Young, modern, highly skilled carpenter needs business card design

I need a business card design for my construction business. Its called 'Pellwright Construction Solutions'. Im looking for a ultra modern design that incorporates P C S, the first letters of the name with only a subtle reference to carpentry. The design should reflect my high quality work and eye for detail. i have also uploaded some exmaple designs i like.

Industry/Entity Type

Construction

Requirements
Must have
• Name of business, my name, mobile number, ABN number, email address
Nice to have
• A logo incorporating the name of the business

```html
<!DOCTYPE html>
<html lang="en">
<head>
<meta charset="UTF-8">
<title>Pellwright Construction Solutions – Business Card</title>
<link href="https://fonts.googleapis.com/css2?family=Exo+2:wght@500;600;700&display=swap" rel="stylesheet">
<style>
  :root {
    --navy: #022a6b;
    --ink: #0a0a0a;
    --paper: #ffffff;
    --backdrop: #e6e7ea;
  }
  * { margin: 0; padding: 0; box-sizing: border-box; }
  html, body {
    width: 1200px;
    height: 900px;
    overflow: hidden;
    background: var(--backdrop);
  }
  .business-card {
    position: absolute;
    left: 100px;
    top: 162px;
    width: 1000px;
    height: 575px;
    background: var(--paper);
    overflow: hidden;
    font-family: "Exo 2", sans-serif;
    box-shadow: 0 6px 18px rgba(0,0,0,0.18);
  }
  .card-wave {
    position: absolute;
    inset: 0;
    width: 100%;
    height: 100%;
  }
  .wave-outline { fill: var(--ink); }
  .wave-gap { fill: var(--paper); }
  .wave-panel { fill: var(--navy); }

  .brand-lockup {
    position: absolute;
    left: 109px;
    top: 78px;
    color: var(--navy);
    font-weight: 700;
  }
  .brand-initials {
    font-size: 138px;
    line-height: 1;
    letter-spacing: 4px;
  }
  .brand-name {
    margin-top: 6px;
    font-size: 22px;
    line-height: 1;
    letter-spacing: 0.3px;
  }

  .contact-block {
    position: absolute;
    right: 72px;
    top: 282px;
    text-align: right;
    color: var(--paper);
  }
  .owner-name {
    font-size: 44px;
    font-weight: 600;
    line-height: 1;
    margin-bottom: 30px;
  }
  .contact-line {
    display: flex;
    justify-content: flex-end;
    align-items: center;
    gap: 12px;
    font-size: 28px;
    font-weight: 500;
    line-height: 1;
    margin-bottom: 24px;
  }
  .contact-icon { fill: var(--paper); flex: none; }
</style>
</head>
<body>
  <div class="business-card">
    <svg class="card-wave" viewBox="0 0 668 383" preserveAspectRatio="none" aria-hidden="true">
      <path class="wave-outline" d="M383,0 C418,50 393,130 350,200 C308,270 288,330 313,383 L668,383 L668,0 Z"/>
      <path class="wave-gap" d="M389,0 C424,50 399,130 356,200 C314,270 294,330 319,383 L668,383 L668,0 Z"/>
      <path class="wave-panel" d="M396,0 C431,50 406,130 363,200 C321,270 301,330 326,383 L668,383 L668,0 Z"/>
    </svg>

    <div class="brand-lockup">
      <div class="brand-initials">PCS</div>
      <div class="brand-name">Pellwright Construction Solutions</div>
    </div>

    <div class="contact-block">
      <div class="owner-name">Mason Pellwright</div>
      <div class="contact-line">ABN: 41 286 553 907</div>
      <div class="contact-line">
        <svg class="contact-icon" width="20" height="34" viewBox="0 0 20 34" aria-hidden="true">
          <rect x="1" y="1" width="18" height="32" rx="3" fill="none" stroke="#fff" stroke-width="2"/>
          <rect x="4" y="4" width="12" height="9" fill="#fff"/>
          <rect x="4" y="16" width="3" height="3"/><rect x="8.5" y="16" width="3" height="3"/><rect x="13" y="16" width="3" height="3"/>
          <rect x="4" y="21" width="3" height="3"/><rect x="8.5" y="21" width="3" height="3"/><rect x="13" y="21" width="3" height="3"/>
          <rect x="4" y="26" width="3" height="3"/><rect x="8.5" y="26" width="3" height="3"/><rect x="13" y="26" width="3" height="3"/>
        </svg>
        043-518-2260
      </div>
      <div class="contact-line">
        <svg class="contact-icon" width="38" height="26" viewBox="0 0 38 26" aria-hidden="true">
          <path d="M0,0 H38 V26 H0 Z M3,3 L19,15 L35,3 Z M2,24 H36 L25,13 L19,18 L13,13 Z" fill-rule="evenodd"/>
        </svg>
        mason_pellwright@mailbox.com
      </div>
    </div>
  </div>
</body>
</html>
```